MerlionTripzy

I need a website similar to http://crestvalora.example. I have the following broad requirements
1. Site should be a itinerary based singapore travel and holiday site. You can visit travquill.example for domain knowledge but not for design. Design should be exact replica of crestvalora.example
2. Site should be same as http://crestvalora.example. Links placement, Logo Placement, Forms design, scrolling, THE MAIN VIDEO LIKE GIF (required and acceptance reqd.), fonts, social links, javascript(copy not reinvent) et al. Please ask as many questions if you have queries. This is very important. I am a CS Grad so won't accept deviation because i know web programming. Design should be exact replica
3. Please use images from Creative Commons travel images from pixhaven or internet especially singapore popular destinations. images will help my sale and please ensure creative quality.
4. Cross Browser importantly IE versions because target customers may be computer illiterates
5. HTML5/css3 and follow latest Standards and practices.
6. Clean Commented HTML and css code for maintainability.

Hoping for the world's best creative and experienced professional who have done similar designs to accept my project.

Industry/Entity Type

Internet

```html
<!DOCTYPE html>
<html lang="en">
<head>
<meta charset="utf-8">
<title>MerlionTripzy – A Five Star Hotel</title>
<link rel="stylesheet" href="https://fonts.googleapis.com/css2?family=Open+Sans:wght@400;600;700&family=Arimo:wght@400;700&display=swap">
<style>
  :root{
    --topbar:#2a2a2a;
    --topbar-text:#9a9a9a;
    --accent:#5bbfca;
    --accent-dark:#3e9ea9;
    --pink:#e53fc2;
    --ink:#4a4a4a;
    --muted:#999;
    --line:#d8d8d8;
    --field:#ccc;
    --white:#fff;
  }
  *{box-sizing:border-box;margin:0;padding:0}
  html,body{width:1200px;height:953px;overflow:hidden;background:var(--white)}
  body{position:relative;font-family:"Open Sans",Arial,sans-serif;color:var(--ink)}

  .topbar{position:absolute;left:0;top:0;width:1200px;height:34px;background:var(--topbar);border-bottom:2px solid var(--accent);font-family:"Arimo",Arial,sans-serif;font-size:10px;color:var(--topbar-text)}
  .topbar .contact{position:absolute;left:93px;top:10px;display:flex;gap:26px;align-items:center}
  .topbar .contact span{display:flex;align-items:center;gap:7px}
  .topbar .lang{position:absolute;left:930px;top:9px;font-size:9px}
  .topbar .social{position:absolute;left:1006px;top:10px;display:flex;gap:18px}
  .topbar .social i{display:block;width:11px;height:11px;border-radius:50%;background:var(--topbar-text)}
  .topbar .divider{position:absolute;top:7px;width:1px;height:18px;background:#444}

  .header{position:absolute;left:0;top:34px;width:1200px;height:74px;background:var(--white);border-bottom:1px solid #e5e5e5}
  .brand{position:absolute;left:96px;top:25px;font-family:"Open Sans",sans-serif;font-weight:700;font-size:17px;letter-spacing:-.3px;color:#222;text-transform:uppercase}
  .header .sep{position:absolute;left:297px;top:0;width:1px;height:74px;background:#e3e3e3}
  .nav{position:absolute;top:29px;left:0;font-size:12.5px;color:#555}
  .nav a{position:absolute;white-space:nowrap;text-decoration:none;color:inherit}
  .nav a.active{color:var(--accent)}
  .caret{display:inline-block;margin-left:5px;border-left:3.5px solid transparent;border-right:3.5px solid transparent;border-top:4px solid #555;vertical-align:middle}

  .hero{position:absolute;left:0;top:108px;width:1200px;height:400px;
    background:
      linear-gradient(180deg,rgba(0,0,0,0) 55%,rgba(0,0,0,.15) 100%),
      linear-gradient(180deg,transparent 0,transparent 62%,#4fb4c9 72%,#8fd8e6 86%,#a57f5c 86.5%,#7d6045 100%),
      linear-gradient(90deg,#d9b978 0%,#e0c88e 30%,#c9a56d 48%,#6f7fa8 60%,#6c7eb5 100%),
      linear-gradient(180deg,#5f74bd 0%,#7d8cc6 40%,#a89889 60%,#3c4a3a 100%);
    background-blend-mode:normal,normal,multiply,normal}
  .hero-title{position:absolute;left:530px;top:30px;width:580px;text-align:center;font-family:"Arimo",Arial,sans-serif;font-weight:700;font-size:37px;color:var(--white);text-shadow:0 1px 3px rgba(0,0,0,.35);display:flex;align-items:center;justify-content:center;gap:8px}
  .stars{display:flex;gap:3px}
  .hero-sub{position:absolute;left:530px;top:92px;width:580px;text-align:center;font-family:"Arimo",Arial,sans-serif;font-size:25px;color:var(--white);text-shadow:0 1px 3px rgba(0,0,0,.35)}
  .btn-rooms{position:absolute;left:770px;top:158px;width:102px;height:40px;background:var(--pink);border-radius:3px;box-shadow:0 2px 0 #a62a8c;color:var(--white);font-weight:700;font-size:12px;text-align:center;line-height:40px}
  .slide-arrow{position:absolute;top:182px;width:34px;height:34px;border-radius:50%;background:rgba(0,0,0,.55)}
  .slide-arrow.prev{left:18px}
  .slide-arrow.next{left:1148px}
  .slide-arrow svg{position:absolute;left:11px;top:9px}

  .booking{position:absolute;left:94px;top:458px;width:1012px;height:107px;background:var(--white);border-radius:3px;box-shadow:0 1px 4px rgba(0,0,0,.18)}
  .field{position:absolute;top:26px}
  .field label{display:flex;align-items:center;gap:8px;font-size:11.5px;font-weight:700;color:#444;height:16px}
  .info{width:13px;height:13px;border-radius:50%;background:#9a9a9a;color:#fff;font-size:9px;text-align:center;line-height:13px;font-weight:700}
  .input{position:relative;margin-top:5px;height:30px;border:1px solid var(--field);border-radius:3px;font-size:12px;color:#aaa;padding:6px 10px;background:#fff}
  .input svg{position:absolute;right:8px;top:8px}
  .select-btn{position:absolute;right:10px;top:6px;width:16px;height:16px;border:1px solid #777;background:#e6e6e6}
  .select-btn::after{content:"";position:absolute;left:4px;top:6px;border-left:3.5px solid transparent;border-right:3.5px solid transparent;border-top:4px solid #222}
  .btn-book{position:absolute;left:843px;top:48px;width:147px;height:30px;border-radius:3px;background:linear-gradient(#86cfd7,#5cb6c0);border:1px solid var(--accent-dark);color:var(--white);font-weight:700;font-size:12.5px;text-align:center;line-height:28px}

  .section-title{position:absolute;left:94px;top:606px;width:1012px;height:28px;text-align:center;font-size:20px;font-weight:700;color:#555}
  .section-title::before,.section-title::after{content:"";position:absolute;top:14px;width:368px;height:1px;background:var(--line)}
  .section-title::before{left:0}
  .section-title::after{right:0}

  .room{position:absolute;top:677px;width:315px;height:252px;border:1px solid #e6e6e6;box-shadow:0 1px 2px rgba(0,0,0,.08);background:#fff}
  .room .photo{height:202px}
  .room .foot{position:relative;height:49px}
  .room .name{position:absolute;left:18px;top:17px;font-size:12.5px;font-weight:700;color:#444}
  .room .price{position:absolute;right:0;top:0;width:75px;height:49px;border-left:1px solid #e6e6e6;text-align:center}
  .room .price b{display:block;margin-top:8px;font-size:16px;font-weight:600;color:var(--accent);line-height:20px}
  .room .price small{display:block;font-size:8.5px;color:var(--muted)}
</style>
</head>
<body>

<div class="topbar">
  <div class="contact">
    <span>
      <svg width="10" height="10" viewBox="0 0 10 10"><path d="M2 0.5 L3.6 2.6 L2.8 3.6 Q4 6 6.4 7.2 L7.4 6.4 L9.5 8 L8.5 9.5 Q3 9 0.5 1.5 Z" fill="#9a9a9a"/></svg>
      05-318624570
    </span>
    <span>
      <svg width="12" height="9" viewBox="0 0 12 9"><rect x="0" y="0" width="12" height="9" fill="#9a9a9a"/><path d="M0 0 L6 5 L12 0" fill="none" stroke="#2a2a2a" stroke-width="1.2"/></svg>
      MAIL@HARBORSTAY.EXAMPLE
    </span>
  </div>
  <div class="divider" style="left:181px"></div>
  <div class="lang">ENGLISH <span class="caret" style="border-top-color:#9a9a9a"></span></div>
  <div class="divider" style="left:994px"></div>
  <div class="social" aria-label="Social links"><i></i><i></i><i></i></div>
</div>

<header class="header">
  <div class="brand">MerlionTripzy</div>
  <div class="sep"></div>
  <nav class="nav">
    <a class="active" style="left:351px">Home</a>
    <a style="left:417px">Rooms<span class="caret"></span></a>
    <a style="left:501px">Features<span class="caret"></span></a>
    <a style="left:593px">Blog<span class="caret"></span></a>
    <a style="left:663px">Gallery</a>
    <a style="left:735px">Contact<span class="caret"></span></a>
  </nav>
</header>

<section class="hero" role="img" aria-label="Hotel terrace at dusk with lit parasols, lounge chairs and a blue swimming pool">
  <h1 class="hero-title">
    <span class="stars">
      <svg width="110" height="20" viewBox="0 0 110 20"><g fill="none" stroke="#fff" stroke-width="1.3"><path id="star" d="M10 1 L12.4 7.2 L19 7.4 L13.8 11.4 L15.6 18 L10 14.2 L4.4 18 L6.2 11.4 L1 7.4 L7.6 7.2 Z"/><use href="#star" x="22"/><use href="#star" x="44"/><use href="#star" x="66"/><use href="#star" x="88"/></g></svg>
    </span>
    A Five Star Hotel
    <span class="stars">
      <svg width="110" height="20" viewBox="0 0 110 20"><g fill="none" stroke="#fff" stroke-width="1.3"><use href="#star"/><use href="#star" x="22"/><use href="#star" x="44"/><use href="#star" x="66"/><use href="#star" x="88"/></g></svg>
    </span>
  </h1>
  <p class="hero-sub">And we like to keep it that way!</p>
  <div class="btn-rooms">SEE ROOMS</div>
  <div class="slide-arrow prev"><svg width="12" height="16" viewBox="0 0 12 16"><path d="M9 1 L3 8 L9 15" fill="none" stroke="#fff" stroke-width="2.6"/></svg></div>
  <div class="slide-arrow next"><svg width="12" height="16" viewBox="0 0 12 16"><path d="M3 1 L9 8 L3 15" fill="none" stroke="#fff" stroke-width="2.6"/></svg></div>
</section>

<form class="booking">
  <div class="field" style="left:22px;width:229px">
    <label>E-mail</label>
    <div class="input">Please enter your E-mail</div>
  </div>
  <div class="field" style="left:268px;width:147px">
    <label>Room Type <span class="info">i</span></label>
    <div class="input">Select a room<span class="select-btn"></span></div>
  </div>
  <div class="field" style="left:432px;width:147px">
    <label>Check-in <span class="info">i</span></label>
    <div class="input">Check-in
      <svg width="13" height="12" viewBox="0 0 13 12"><rect x="0.5" y="1.5" width="12" height="10" fill="none" stroke="#5bbfca"/><rect x="0.5" y="1.5" width="12" height="3" fill="#5bbfca"/><path d="M3 6.5h2M6 6.5h2M9 6.5h2M3 9h2M6 9h2M9 9h2" stroke="#5bbfca"/></svg>
    </div>
  </div>
  <div class="field" style="left:597px;width:147px">
    <label>Check-out <span class="info">i</span></label>
    <div class="input">Check-out
      <svg width="13" height="12" viewBox="0 0 13 12"><rect x="0.5" y="1.5" width="12" height="10" fill="none" stroke="#5bbfca"/><rect x="0.5" y="1.5" width="12" height="3" fill="#5bbfca"/><path d="M3 6.5h2M6 6.5h2M9 6.5h2M3 9h2M6 9h2M9 9h2" stroke="#5bbfca"/></svg>
    </div>
  </div>
  <div class="field" style="left:761px;width:64px">
    <label>Guests</label>
    <div class="input">1
      <svg width="10" height="11" viewBox="0 0 10 11"><circle cx="5" cy="3" r="2.6" fill="#5bbfca"/><path d="M0.5 11 Q0.5 6 5 6 Q9.5 6 9.5 11 Z" fill="#5bbfca"/></svg>
    </div>
  </div>
  <div class="btn-book">BOOK NOW</div>
</form>

<h2 class="section-title">Guests Favorite Rooms</h2>

<article class="room" style="left:94px">
  <div class="photo" role="img" aria-label="Double bedroom with bedside lamp and a glass door opening onto a sea-view terrace" style="background:linear-gradient(90deg,#c9b9a3 0%,#e4ddd0 35%,#9cc3d8 60%,#6f9a7b 85%,#3f7f86 100%)"></div>
  <div class="foot"><span class="name">Double bedroom</span><div class="price"><b>€ 99</b><small>a night</small></div></div>
</article>

<article class="room" style="left:441px">
  <div class="photo" role="img" aria-label="King size bedroom lounge with chairs and panoramic windows over a lake and mountains" style="background:linear-gradient(180deg,#5fa7d8 0%,#9fcbe6 35%,#4d7e8e 55%,#2e5e70 70%,#d9d4cc 100%)"></div>
  <div class="foot"><span class="name">King Size Bedroom</span><div class="price"><b>€ 149</b><small>a night</small></div></div>
</article>

<article class="room" style="left:788px">
  <div class="photo" role="img" aria-label="Bright single room with white sofa, television and a view of the coast" style="background:linear-gradient(180deg,#e9eef0 0%,#a7c9d6 30%,#7fa98c 50%,#eef1f2 70%,#dfe3e5 100%)"></div>
  <div class="foot"><span class="name">Single room</span><div class="price"><b>€ 120</b><small>a night</small></div></div>
</article>

</body>
</html>
```